" Sou formada ha 12 anos e ha 3 anos inaugurei a clinica onde realizo atendimento em todas as especilidades odontologicas. Sou responsavel por fazer as avaliacoes e pelo tratamento ortodontico, trouxe outros colegas para trabalharem comigo que possuem outras especialidades como: periodontia, estetica, implantodontia... O objetivo e promover tratamento qualificado aos pacientes que nos procuram. Todos os profissionais possuem titulo de especialista e sao formados ha mais de 10 anos. "

```html
<!DOCTYPE html>
<html lang="pt-BR">
<head>
<meta charset="utf-8">
<title>Serena Odonto – Papel Timbrado</title>
<link rel="stylesheet" href="https://fonts.googleapis.com/css2?family=Montserrat:wght@500&display=swap">
<style>
  :root {
    --backdrop: #ece9e4;
    --paper: #ffffff;
    --navy: #2f3f63;
    --orange: #f08a4b;
    --orange-soft: #f6b48c;
    --navy-soft: #7a869e;
    --steel-dark: #9a9ca1;
    --steel-light: #f1f1f2;
  }
  * { margin: 0; padding: 0; box-sizing: border-box; }
  html, body {
    width: 1200px;
    height: 1200px;
    overflow: hidden;
    background: var(--backdrop);
  }
  .stationery {
    position: relative;
    width: 1200px;
    height: 1200px;
  }
  .letterhead {
    position: absolute;
    top: 290px;
    width: 420px;
    height: 590px;
    background: var(--paper);
    box-shadow: 0 6px 18px rgba(0, 0, 0, 0.18);
    overflow: hidden;
  }
  .letterhead--classic { left: 140px; }
  .letterhead--banded { left: 640px; }

  .brand-name {
    position: absolute;
    font-family: "Montserrat", sans-serif;
    font-weight: 500;
    font-size: 20px;
    letter-spacing: 0;
    color: var(--navy);
    white-space: nowrap;
  }
  .letterhead--classic .brand-name { top: 54px; left: 34px; }
  .letterhead--banded .brand-name { top: 52px; left: 0; right: 0; text-align: center; }

  .top-band {
    position: absolute;
    top: 0; left: 0; right: 0;
    height: 26px;
    background: linear-gradient(180deg, var(--steel-dark), var(--steel-light));
  }
  .bottom-band {
    position: absolute;
    left: 0; right: 0;
    top: 500px;
    height: 60px;
    background: linear-gradient(180deg, var(--steel-dark), var(--steel-light) 85%, var(--paper));
  }
  .accent-strip {
    position: absolute;
    height: 44px;
    border-radius: 22px;
  }
  .letterhead--classic .accent-strip {
    top: 466px;
    left: 8px; right: 8px;
    background: linear-gradient(90deg, var(--orange) 0%, var(--orange) 46%, var(--navy) 54%, var(--navy) 100%);
  }
  .letterhead--banded .accent-strip {
    top: 478px;
    left: 14px; right: 14px;
    background: linear-gradient(90deg, var(--orange-soft) 0%, var(--orange-soft) 46%, var(--navy-soft) 54%, var(--navy-soft) 100%);
  }
</style>
</head>
<body>
  <main class="stationery">
    <section class="letterhead letterhead--classic">
      <h1 class="brand-name">Serena Odonto</h1>
      <div class="bottom-band"></div>
      <div class="accent-strip" role="img" aria-label="Faixa decorativa de círculos laranja e azul-marinho"></div>
    </section>

    <section class="letterhead letterhead--banded">
      <div class="top-band"></div>
      <h1 class="brand-name">Serena Odonto</h1>
      <div class="accent-strip" role="img" aria-label="Faixa decorativa de círculos em tons suaves de laranja e azul"></div>
    </section>
  </main>
</body>
</html>
```